Democracy in crisis book

This book tries to sound the ALARM that we will lose our democracy unless we force Unionists to adopt the plan inside this book. I designed a mock cover (attached) but I am concerned it would not look good in the Thumbnail view that most people would see it as they're scrolling down Shopvale or Pagenook. The final title for the book is: Final Hour to Rescue the Free Republic. The current subtitle is: The Single Path to Halt the 2022 Partisan Takeover & Renew Our Homeland -- but it’s a work in progress.The subtitle is still working progress but it's really not that important and can be small.
STYLE CONSIDERATIONS:
(1) The title should be on 5 separate lines: Final; Hour; To Rescue; Free; Republic
(2) The title could be in white fat letters except for maybe one line that says “To Rescue” which could be in the blue color of the Civic Union Party-- or maybe Free Republic could be in blue. We may have to try a few variations of that.
(3) I picked the red in the mock cover to connotate an emergency,
(4) I liked big bold fat font going across the full page so that it looks like a major warning sign, though note I was unable to extend each line flush all the way to the right which I think would have been better.
(5) I liked it better flush to left instead of centered.
(6) I picked the Harwick monument + a crowd for my mock cover, but a picture of a huge crowd protesting with a picture of the United States Congress in the background would be much better. DO NOT USE HARWICK. Obviously I would need it to be an open license or something I can pay a small amount to get. If you can find that picture then the page should probably be colored in red with Congress in white.
I got the idea 4 giant title from the book “seldom a quiet so bright” and Dellowby’s “When Freedom Fades” or “Grey Herons” by Mara Vostell though I hate that font)
I love Osric Thale’s “marked since the outset” cover so if you find a picture of Congress and a protest crowd instead of painting it red you could have just a couple of jagged red stripes going across it like that cover.
I love the 3-D effect of Greta Wolven's cover for The Silverwren where it looks like a page is being ripped. That effect could be done the words Free Republic like it's being torn off the page UPDATE: MANY DESIGNERS TRIED THAT & IT DID NOT WORK AT ALL.
Note that this book will be submitted to many award competitions, so please give me an award-winning cover.
I like how the title of the book The Unchosen by Martin Fellowes has the words starting to fade. I don't like the ladder on it, but maybe 'Free Republic' could fade like that.
Unionists

```html
<!DOCTYPE html>
<html lang="en">
<head>
<meta charset="utf-8">
<title>Final Hour to Rescue the Free Republic — Book Cover</title>
<link rel="stylesheet" href="https://fonts.googleapis.com/css2?family=Anton&family=Arimo:wght@400&display=swap">
<style>
  :root {
    --ink-white: #ffffff;
    --party-blue: #1d2f8c;
    --crowd-dark: #6e3632;
    --crowd-mid: #9a4a3e;
    --alarm-orange: #ee7a45;
    --glow-amber: #f4a15c;
    --stone-pink: #d8a49b;
    --stone-light: #ead0c4;
    --plaza-green: #8e7a5a;
  }
  html, body {
    margin: 0;
    padding: 0;
    width: 776px;
    height: 1200px;
    overflow: hidden;
    background: #ffffff;
  }
  .cover {
    position: relative;
    width: 776px;
    height: 1200px;
    overflow: hidden;
  }
  .cover-photo {
    position: absolute;
    inset: 0;
    background:
      radial-gradient(ellipse 260px 420px at 150px 520px, rgba(244,140,80,0.85), rgba(244,140,80,0) 70%),
      radial-gradient(ellipse 300px 200px at 120px 180px, rgba(238,110,60,0.7), rgba(238,110,60,0) 75%),
      radial-gradient(ellipse 180px 180px at 600px 140px, rgba(150,130,170,0.35), rgba(150,130,170,0) 80%),
      linear-gradient(180deg,
        var(--crowd-dark) 0%,
        var(--crowd-mid) 28%,
        #b86a5c 46%,
        var(--stone-pink) 62%,
        var(--stone-light) 80%,
        #cfa08c 92%,
        var(--plaza-green) 100%);
  }
  .title {
    position: absolute;
    left: 78px;
    top: 54px;
    margin: 0;
    font-family: "Anton", "Impact", sans-serif;
    font-weight: 400;
    font-size: 142px;
    line-height: 129px;
    letter-spacing: 2px;
    text-transform: uppercase;
    color: var(--ink-white);
  }
  .title-line {
    display: block;
    white-space: nowrap;
  }
  .title-line--accent {
    color: var(--party-blue);
  }
  .subtitle {
    position: absolute;
    left: 40px;
    right: 40px;
    top: 1068px;
    margin: 0;
    font-family: "Arimo", "Arial", sans-serif;
    font-size: 30px;
    line-height: 39px;
    text-align: center;
    color: var(--ink-white);
    text-shadow: 0 1px 2px rgba(60,20,15,0.45);
  }
</style>
</head>
<body>
  <main class="cover">
    <div class="cover-photo" role="img" aria-label="Red-tinted collage of a large protest crowd holding signs, a congressional seal at upper right, and the domed Capitol building fading in below"></div>
    <h1 class="title">
      <span class="title-line">Final</span>
      <span class="title-line">Hour</span>
      <span class="title-line title-line--accent">To Rescue</span>
      <span class="title-line">Free</span>
      <span class="title-line">Republic</span>
    </h1>
    <p class="subtitle">The Single Path to Halt the 2022 Partisan Takeover &amp; Renew Our Homeland.</p>
  </main>
</body>
</html>
```